A5 Personal trainer profile for corbell vitality

I need a A5 Landscape profile designed for the company I work for. Company name is Corbell Vitality. The profile is for personal trainers to let people know:

1. Brief description of themselves
2. Qualifications

A picture will be required on the right hand side of the profile. Corbell Vitality colours are green and white.

The Corbell Vitality Logo in the boarder of the example included must remain. We are looking for a clinical and professional design.

Industry/Entity Type

Health

```html
<!DOCTYPE html>
<html lang="en">
<head>
<meta charset="utf-8">
<title>Personal Trainer Profile – Corbell Vitality</title>
<link href="https://fonts.googleapis.com/css2?family=Rammetto+One&family=Source+Sans+3:wght@400;600&display=swap" rel="stylesheet">
<style>
  :root {
    --green: #4cb848;
    --green-mid: #2e9a3f;
    --green-deep: #0b6a36;
    --green-pale: #eaf2c2;
    --photo-tone: #c6ec7c;
    --ink: #3a3a3a;
    --white: #ffffff;
    --backdrop-centre: #6a6a6a;
    --backdrop-edge: #000000;
  }
  * { margin: 0; padding: 0; box-sizing: border-box; }
  html, body { width: 1200px; height: 999px; overflow: hidden; }
  body {
    position: relative;
    background: radial-gradient(ellipse 640px 560px at 50% 50%, var(--backdrop-centre) 0%, #2a2a2a 70%, var(--backdrop-edge) 100%);
    font-family: "Source Sans 3", "Myriad Pro", sans-serif;
  }
  .profile-card {
    position: absolute; left: 105px; top: 150px;
    width: 990px; height: 699px;
    background: var(--white);
    overflow: hidden;
  }
  .card-art { position: absolute; left: 0; top: 0; }
  .heading-font { font-family: "Rammetto One", "Gill Sans Ultra Bold", sans-serif; }
  .intro-band {
    position: absolute; left: 0; top: 210px; width: 500px; height: 162px;
    background: var(--green-pale);
  }
  .section-title {
    position: absolute; left: 43px;
    font-family: "Rammetto One", sans-serif;
    color: var(--green-mid); font-size: 21px; letter-spacing: -0.2px;
  }
  .services { position: absolute; left: 48px; top: 250px; list-style: none; }
  .services li {
    display: flex; align-items: center;
    font-size: 18.5px; color: var(--ink); line-height: 24px;
  }
  .services li svg { width: 20px; height: 14px; margin-right: 24px; }
  .testimonial {
    position: absolute; left: 42px; top: 410px; width: 460px;
    font-size: 18.5px; line-height: 24px; color: var(--ink);
  }
  .qualifications-band {
    position: absolute; left: 0; top: 538px; width: 990px; height: 161px;
    background: linear-gradient(90deg, var(--green-deep) 0%, #0a7038 45%, var(--green) 82%);
  }
  .qualifications-title {
    position: absolute; left: 33px; top: 17px;
    font-family: "Rammetto One", sans-serif; color: var(--white); font-size: 21px;
  }
  .qualifications { position: absolute; left: 33px; top: 46px; list-style: none; }
  .qualifications li { font-size: 18.5px; line-height: 24px; color: var(--white); display: flex; }
  .qualifications li::before { content: "•"; font-size: 12px; width: 60px; }
  .brand-mark {
    position: absolute; left: 601px; top: 9px; width: 379px; height: 43px;
    background: var(--white);
    display: flex; align-items: center; gap: 10px; padding-left: 4px;
  }
  .brand-mark .brand-square { width: 33px; height: 33px; background: var(--green-mid); }
  .brand-mark .brand-name {
    font-family: "Source Sans 3", sans-serif; font-weight: 600;
    font-size: 36px; color: var(--green-mid); line-height: 1;
  }
</style>
</head>
<body>
<main class="profile-card">
  <svg class="card-art" width="990" height="538" viewBox="0 0 990 538">
    <defs>
      <linearGradient id="title-fill" x1="0" y1="0" x2="0" y2="1">
        <stop offset="0" stop-color="#0b6a36"/>
        <stop offset="0.55" stop-color="#3aa842"/>
        <stop offset="1" stop-color="#6ccc52"/>
      </linearGradient>
      <linearGradient id="ring-fill" x1="0" y1="0" x2="1" y2="0">
        <stop offset="0" stop-color="#0b6a36"/>
        <stop offset="1" stop-color="#4cb848"/>
      </linearGradient>
      <clipPath id="photo-clip"><circle cx="898" cy="320" r="402"/></clipPath>
    </defs>
    <circle cx="890" cy="320" r="420" fill="url(#ring-fill)"/>
    <circle cx="898" cy="322" r="410" fill="#ffffff"/>
    <circle cx="898" cy="320" r="404" fill="var(--green)"/>
    <rect x="480" y="0" width="510" height="538" fill="var(--photo-tone)" clip-path="url(#photo-clip)"
          role="img" aria-label="Portrait photo of the personal trainer, smiling, wearing a green polo shirt"/>
    <text class="heading-font" x="42" y="60" font-size="50" fill="var(--green)" textLength="322" lengthAdjust="spacingAndGlyphs">PERSONAL</text>
    <text class="heading-font" x="42" y="140" font-size="86" fill="url(#title-fill)" textLength="444" lengthAdjust="spacingAndGlyphs">TRAINER</text>
    <text class="heading-font" x="115" y="195" font-size="46" fill="var(--green-mid)" textLength="376" lengthAdjust="spacingAndGlyphs">MARCUS ODENYA</text>
  </svg>

  <section class="intro-band" aria-hidden="true"></section>
  <h2 class="section-title" style="top:217px">How I can help you?</h2>
  <ul class="services">
    <li><svg viewBox="0 0 20 14"><path d="M0 5h11V0l9 7-9 7V9H0z" fill="#4cb848"/></svg>Reduce body fat&nbsp; and increase body definition</li>
    <li><svg viewBox="0 0 20 14"><path d="M0 5h11V0l9 7-9 7V9H0z" fill="#4cb848"/></svg>Increase stamina, improve agility and speed</li>
    <li><svg viewBox="0 0 20 14"><path d="M0 5h11V0l9 7-9 7V9H0z" fill="#4cb848"/></svg>Increase strength and size</li>
    <li><svg viewBox="0 0 20 14"><path d="M0 5h11V0l9 7-9 7V9H0z" fill="#4cb848"/></svg>Plyometric training and conditioning</li>
    <li><svg viewBox="0 0 20 14"><path d="M0 5h11V0l9 7-9 7V9H0z" fill="#4cb848"/></svg>Flexibility and core strength</li>
  </ul>

  <h2 class="section-title" style="top:378px">What my clients say about me?</h2>
  <blockquote class="testimonial">&nbsp;"With Marcus my training is always challenging and fun. I don’t remember a session to be boring or repetitive. In short time I improved my core strength and flexibility. I can run 10k without stopping. It is amazing improvement.&nbsp; " Laura Whitcombe</blockquote>

  <section class="qualifications-band">
    <h2 class="qualifications-title">Qualifications</h2>
    <ul class="qualifications">
      <li>Advanced Circuit Training</li>
      <li>Advanced Diploma in Personal Training - Level 3 PTRS Registered</li>
      <li>Fitness Instructor - Level 2 PTRS Registered</li>
      <li>Also qualified in – Suspension training, Studio Cycling, Sports Nutrition, Weight Management</li>
    </ul>
    <div class="brand-mark">
      <span class="brand-square" aria-hidden="true"></span>
      <span class="brand-name">Corbell Vitality</span>
    </div>
  </section>
</main>
</body>
</html>
```